Logo and Business Card Design

We are macadamia farmers with a network of operations able to deliver macadamia nuts to you!
Be it wholesale or retail supply, our production capacity, network of farms and processing facilities is able to provide reliable and secure supply of macadamia products.
We have a network of owned and contract production macadamia farms located throughout Queensland and New South Wales. Our farms are located in the lush green hinterland area of Northern New south wales and the rich and productive farmlands of the Burnett area of southern Queensland. We pride ourselves on our environmentally sensitive production systems, the ownership and pride in which our network of farmers care for their orchards and the food we produce. Collectively our farms deliver to processing facilities able to provide macadamia nut in shell and kernel in wholesale and retail quantities.
Our point of difference is our integrated supply chain, delivering paddock to plate capacity.
The enterprise is a true network in that we have combined production, processing and marketing expertise into a one stop shop!
Our design should communicate our network capacity, we are a food producer which is respectful of the land and the environment in which we operate.
Our focus is Macadamia nut production, we farm and process Macadamia's where they are a native tree.

The draft design concept we feel is too mechanical and sterile, its time for something fresh and exciting!

Environment

Tellow Grove Pty. Ltd
An Integrated Macadamia production Enterprise.

```html
<!DOCTYPE html>
<html lang="en">
<head>
<meta charset="utf-8">
<title>Tellow Grove – Business Card</title>
<link rel="stylesheet" href="https://fonts.googleapis.com/css2?family=Play:wght@400;700&family=Arimo:wght@400&display=swap">
<style>
  :root {
    --backdrop: #e6e6e1;
    --card-white: #ffffff;
    --ink-brown: #2e2119;
    --ink-soft: #3a2c22;
    --leaf-green: #22a04b;
    --band-grey: #b1b1aa;
    --band-green: #b8c892;
  }
  * { box-sizing: border-box; margin: 0; padding: 0; }
  html, body {
    width: 1200px;
    height: 902px;
    overflow: hidden;
    background: var(--backdrop);
  }
  .card {
    position: absolute;
    left: 50px;
    top: 136px;
    width: 1100px;
    height: 629px;
    background: var(--card-white);
    box-shadow: 0 6px 24px rgba(0, 0, 0, 0.12);
    overflow: hidden;
  }
  .card__header {
    position: absolute;
    left: 0; top: 0;
    width: 100%;
    height: 213px;
    background: var(--card-white);
  }
  .brand {
    position: absolute;
    left: 82px;
    top: 40px;
    display: flex;
    align-items: center;
    gap: 22px;
  }
  .brand__name {
    font-family: "Play", sans-serif;
    font-weight: 700;
    font-size: 60px;
    line-height: 60px;
    letter-spacing: 3px;
    text-transform: uppercase;
    color: var(--ink-brown);
  }
  .brand__dot {
    width: 46px;
    height: 46px;
    border-radius: 50%;
    background: var(--leaf-green);
    align-self: flex-end;
    margin-bottom: 8px;
  }
  .card__band {
    position: absolute;
    left: 0; top: 213px;
    width: 100%;
    height: 322px;
    background: linear-gradient(15deg, var(--band-green) 0%, #b6bf9f 35%, var(--band-grey) 70%);
  }
  .holder {
    position: absolute;
    left: 82px;
    top: 98px;
    width: 410px;
  }
  .holder__name {
    font-family: "Play", sans-serif;
    font-weight: 400;
    font-size: 50px;
    line-height: 56px;
    color: var(--ink-brown);
    white-space: nowrap;
  }
  .holder__address {
    font-family: "Arimo", sans-serif;
    font-size: 29px;
    line-height: 38px;
    color: var(--ink-soft);
    text-align: right;
    margin-top: 4px;
    white-space: nowrap;
  }
  .contacts {
    position: absolute;
    left: 610px;
    top: 108px;
    list-style: none;
  }
  .contacts__item {
    display: flex;
    align-items: center;
    gap: 22px;
    height: 45px;
    font-family: "Arimo", sans-serif;
    font-size: 32px;
    color: var(--ink-soft);
    white-space: nowrap;
  }
  .contacts__icon {
    width: 25px;
    height: 25px;
    flex: none;
  }
  .card__footer {
    position: absolute;
    left: 0; bottom: 0;
    width: 100%;
    height: 94px;
    background: var(--card-white);
    display: flex;
    align-items: center;
    justify-content: center;
  }
  .tagline {
    font-family: "Arimo", sans-serif;
    font-size: 38px;
    color: var(--ink-brown);
    white-space: nowrap;
  }
</style>
</head>
<body>
  <article class="card">
    <header class="card__header">
      <div class="brand">
        <div class="brand__name">Tellow<br>Grove</div>
        <span class="brand__dot"></span>
      </div>
    </header>

    <section class="card__band">
      <div class="holder">
        <h1 class="holder__name">Daniel Whitcombe</h1>
        <p class="holder__address">14 Ridge Road Orchard Lane<br>Gayndah, QLD 4625</p>
      </div>

      <ul class="contacts">
        <li class="contacts__item">
          <svg class="contacts__icon" viewBox="0 0 24 24" aria-hidden="true">
            <rect width="24" height="24" fill="var(--leaf-green)"/>
            <path d="M8 5.5l2.2 2.6-1.3 1.7c.9 2 2.4 3.5 4.3 4.4l1.7-1.3 2.6 2.2-1.4 2.4c-4.8-.4-9.2-4.8-9.6-9.6z" fill="#fff"/>
          </svg>
          <span>0400 918 226</span>
        </li>
        <li class="contacts__item">
          <svg class="contacts__icon" viewBox="0 0 24 24" aria-hidden="true">
            <rect width="24" height="24" fill="var(--leaf-green)"/>
            <rect x="5" y="7.5" width="14" height="9" fill="none" stroke="#fff" stroke-width="1.6"/>
            <path d="M5 7.5l7 5 7-5" fill="none" stroke="#fff" stroke-width="1.6"/>
          </svg>
          <span>hello@tellowgrove.com.au</span>
        </li>
        <li class="contacts__item">
          <svg class="contacts__icon" viewBox="0 0 24 24" aria-hidden="true">
            <rect width="24" height="24" fill="var(--leaf-green)"/>
            <circle cx="12" cy="12" r="6.5" fill="none" stroke="#fff" stroke-width="1.6"/>
            <ellipse cx="12" cy="12" rx="2.8" ry="6.5" fill="none" stroke="#fff" stroke-width="1.3"/>
            <path d="M5.5 12h13" stroke="#fff" stroke-width="1.3"/>
          </svg>
          <span>www.tellowgrove.com.au</span>
        </li>
      </ul>
    </section>

    <footer class="card__footer">
      <p class="tagline">An Integrated Macadamia production Enterprise</p>
    </footer>
  </article>
</body>
</html>
```